International Digitally Led Media Agency Requires a New Website

Brief Outline

• We are a growing business that has been established for approximately 2 years.

• Our current website did the job when Brindle Media began but it has not developed and progressed alongside the business (currently it does not represent nor portray the business appropriately).

• Brindle Media is a digitally led media agency that has numerous arms; 1) production based work (e.g. Paid Advertising, etc.) 2) consultancy and 3) Offline media (such as outdoor, TV, Radio)

• The business is globally focused and the website must reflect this.

• The new website is to portray the business more professionally with thought leadership at the forefront.

• The tone and voice of the website is to be clear, concise and straight talking.

• The website isn't to be a driver of new business (e.g. conversion based for enquiries) but is to support external new business activities. However, the website is to support the thought leadership marketing (specifically around content marketing - webinars, whitepapers, social, etc).

• We must be able to edit/upload/add content to the website very easily.

The current website is www.brindle-media.example

Current clients include
K&T - www.k&t.example
Hollings Marlowe - www.hm.example
QV Heard - www.qvheard.example
Lunglight UK - www.lunglight.example.uk
The Gripwell Academy - www.gripwell-academy.example.uk
Tilo Pensions - www.tilopensions.example
Cobble Loans - www.cobbleloans.example.uk
KRMaltex - www.kr-maltex.example.uk
Wayfarer Lodging Collective - www.wlc.example
Quillmark - www.quillmark.example
Varnish Lane - www.varnishlaneit.example

Reason: We gave some delayed feedback to some desginers looking to enter the project and want to give them a chance to submit their designs.

Target Market(s)

Key decision makers within brands. Marketing Executives/Managers/Directors, Procurement Executives/Managers/Directors, Company Owners, CEO's /MD's

Industry/Entity Type

Business

Coding

Coded - Design and coding required

Number of Pages Required

5+ page

Font styles to use
Sans Serif

Requirements
Must have
• We definitely want video capability and the ability to add pages ourselves.
• We would like the layout to look something like
• HOME
•   
• 7degree3 > CASE STUDIES
• WHAT WE DO > CASE STUDIES
•  
• CONTACT
•  
• CLIENT LOGIN
Nice to have
• Social feeds

```html
<!DOCTYPE html>
<html lang="en">
<head>
<meta charset="utf-8">
<title>Brindle Media</title>
<link rel="stylesheet" href="https://fonts.googleapis.com/css2?family=Oswald:wght@500&family=Open+Sans:wght@400;600;700&family=Raleway:wght@300;400;500&display=swap">
<style>
:root{
  --crimson:#9b1536;
  --ink:#333333;
  --muted:#777777;
  --paper:#ffffff;
  --mist:#f2f2f2;
  --topbar:#ececec;
  --slate:#5b5b5a;
  --strip:#dddddd;
  --night:#050505;
  --nav-active:#6b6b6b;
  --yellow:#f5c518;
  --blue:#2b8fd6;
  --grey-ring:#7a7a7a;
}
*{box-sizing:border-box;margin:0;padding:0}
html,body{width:1200px;height:3358px;overflow:hidden}
body{font-family:"Open Sans",Arial,sans-serif;color:var(--ink);background:var(--paper);position:relative}
a{color:inherit;text-decoration:none}

/* top bar */
.topbar{height:45px;background:var(--topbar);display:flex;align-items:center;justify-content:space-between;padding:0 78px}
.social{display:flex;gap:22px}
.social span{width:16px;height:16px;border-radius:50%;background:var(--crimson);display:block}
.social span+span{background:#555}
.login{font-size:15px;color:#777;display:flex;align-items:center;gap:8px}

/* header */
.header{height:101px;display:flex;align-items:center;justify-content:space-between;padding:0 78px}
.brand{font-family:"Open Sans",sans-serif;font-weight:600;font-size:22px;color:#444}
.call{display:flex;align-items:center;gap:14px;font-family:"Open Sans",sans-serif}
.call-label{color:var(--crimson);font-size:24px}
.call-icon{width:48px;height:48px;border-radius:50%;border:2px solid #333;display:flex;align-items:center;justify-content:center}
.call-number{color:var(--crimson);font-size:24px;font-weight:700}

/* nav */
.mainnav{height:56px;background:var(--crimson);display:flex;padding-left:78px}
.mainnav a{color:#fff;font-family:"Raleway",sans-serif;font-size:17px;display:flex;align-items:center;padding:0 26px;text-transform:uppercase}
.mainnav a.active{background:var(--nav-active)}
.mainnav a+a{margin-left:20px}

/* hero */
.hero{height:575px;position:relative;background:radial-gradient(ellipse at 72% 78%,#ffffff 0,#cfe3ff 6%,#3c6aa8 18%,#182a52 34%,#070a18 60%,#02030a 100%)}
.hero-text{position:absolute;left:78px;top:190px;color:#fff}
.hero-title{font-family:"Oswald",sans-serif;font-weight:500;font-size:62px;letter-spacing:3px;line-height:1}
.hero-sub{font-size:24px;margin-top:22px}
.btn{display:inline-flex;align-items:center;gap:12px;border-radius:26px;font-family:"Open Sans",sans-serif;font-weight:600;text-transform:uppercase}
.btn-crimson{background:var(--crimson);color:#fff}
.hero .btn{margin-top:30px;height:50px;padding:0 22px;font-size:17px}

/* services */
.services{height:230px;background:var(--mist);display:flex;padding:36px 0 0 78px;gap:32px}
.service{width:237px;display:flex;gap:8px}
.service-icon{width:94px;height:94px;flex:none}
.service h3{font-family:"Raleway",sans-serif;font-weight:400;font-size:22px;color:var(--crimson);line-height:1.2}
.service p{font-size:13px;color:#555;line-height:1.75;margin-top:6px}

/* welcome */
.welcome{height:368px;position:relative;padding:50px 78px 0}
.section-title{font-family:"Raleway",sans-serif;font-weight:300;font-size:44px;letter-spacing:1px}
.welcome .section-title span{color:var(--crimson);font-weight:400}
.welcome p{width:665px;font-size:15px;line-height:1.85;color:#666;margin-top:24px}
.welcome .btn{margin-top:26px;height:46px;padding:0 26px;font-size:17px}
.welcome-mark{position:absolute;right:120px;top:140px;font-family:"Open Sans",sans-serif;font-weight:600;font-size:36px;color:var(--crimson)}

/* our work */
.work{height:555px;background:var(--crimson);color:#fff;text-align:center;padding-top:46px}
.work .section-title{color:#fff}
.work .lead{font-size:16px;margin-top:24px}
.work-grid{display:flex;gap:38px;justify-content:center;margin-top:40px}
.work-card{width:323px}
.work-photo{height:186px}
.work-card h3{font-family:"Raleway",sans-serif;font-weight:400;font-size:24px;margin-top:20px}
.work-card p{font-size:15px;line-height:1.7;margin-top:6px}

/* clients */
.clients{height:161px;background:var(--strip);display:flex;align-items:center;justify-content:space-between;padding:0 78px}
.client{display:flex;align-items:center;gap:10px;font-family:"Open Sans",sans-serif;font-weight:600;font-size:20px;color:#2d3a66}
.client i{width:26px;height:26px;border-radius:50%;background:#2d3a66;display:block}
.badge{display:block}
.badge-navy{width:82px;height:100px;background:#1d3f7a;border:3px solid #fff;outline:1px solid #1d3f7a}
.badge-black{width:82px;height:82px;background:#111}

/* who we are */
.who{height:495px;background:var(--slate);color:#fff;text-align:center;padding-top:46px;position:relative}
.who .section-title{color:#fff}
.who .lead{font-size:16px;margin-top:20px}
.video{position:absolute;left:100px;top:193px;width:460px;height:257px;background:linear-gradient(#2b2b2b 0 9%,#f4f4f4 9% 92%,#bdbdbd 92%);border-radius:6px}
.video-play{position:absolute;left:208px;top:104px;width:46px;height:46px;border-radius:50%;background:var(--crimson)}
.who-copy{position:absolute;left:590px;top:158px;text-align:left;width:530px}
.who-badges{display:flex;gap:50px}
.who-badges .badge-navy{width:66px;height:78px}
.who-badges .badge-black{width:66px;height:66px}
.who-copy p{font-size:15px;line-height:1.7;margin-top:26px}
.who-copy p+p{margin-top:0}
.btn-white{background:#fff;color:var(--crimson);height:50px;padding:0 24px;font-size:19px;margin-top:28px}

/* blog */
.blog{height:499px;text-align:center;padding-top:46px}
.blog .section-title{color:var(--crimson);font-weight:400}
.blog-grid{display:flex;gap:38px;padding-left:78px;margin-top:36px;text-align:left}
.post{width:233px}
.post-photo{height:141px}
.post h3{font-size:15px;font-weight:400;color:var(--crimson);line-height:1.65;margin-top:12px}
.post time{display:flex;align-items:center;gap:6px;font-size:14px;color:#999;margin-top:2px}
.post p{font-size:15px;color:#777;line-height:1.7;margin-top:8px}

/* footer */
.footer{height:224px;background:var(--night);color:#fff;padding:0 78px}
.footer-nav{height:72px;display:flex;align-items:center;justify-content:space-between;border-bottom:1px solid #333}
.footer-links{display:flex;gap:30px;font-size:15px}
.footer-social{display:flex;gap:30px}
.footer-social span{width:18px;height:18px;border-radius:50%;background:#fff;display:block}
.footer-social span:first-child{background:var(--crimson)}
.footer h4{font-family:"Raleway",sans-serif;font-weight:400;font-size:24px;margin-top:18px}
.contact-row{display:flex;justify-content:space-between;margin-top:18px;font-size:14px;align-items:center}
.contact-item{display:flex;align-items:center;gap:14px;line-height:1.4}
.contact-icon{width:40px;height:40px;border-radius:50%;background:#fff;display:flex;align-items:center;justify-content:center;flex:none}
.contact-icon.red{background:var(--crimson)}
.copyright{height:49px;background:var(--crimson);color:#fff;display:flex;align-items:center;justify-content:center;font-size:15px}
</style>
</head>
<body>

<div class="topbar">
  <div class="social" aria-label="Social links"><span></span><span></span><span></span><span></span></div>
  <a class="login" href="#"><svg width="14" height="14" viewBox="0 0 14 14"><path d="M1 7h8M6 4l3 3-3 3M9 1h4v12H9" fill="none" stroke="#777" stroke-width="1.6"/></svg>Login</a>
</div>

<header class="header">
  <div class="brand">Brindle Media</div>
  <div class="call">
    <span class="call-label">Call us now</span>
    <span class="call-icon"><svg width="22" height="22" viewBox="0 0 24 24"><path d="M6.6 10.8a15 15 0 0 0 6.6 6.6l2.2-2.2c.3-.3.7-.4 1-.2 1.1.4 2.3.6 3.6.6.6 0 1 .4 1 1V20c0 .6-.4 1-1 1A17 17 0 0 1 3 4c0-.6.4-1 1-1h3.5c.6 0 1 .4 1 1 0 1.3.2 2.5.6 3.6.1.3 0 .7-.2 1z" fill="#333"/></svg></span>
    <span class="call-number">+44 207 555 0143</span>
  </div>
</header>

<nav class="mainnav">
  <a class="active" href="#">Home</a><a href="#">About</a><a href="#">Our Work</a><a href="#">Who We Are</a><a href="#">Client Login</a><a href="#">Contact</a>
</nav>

<section class="hero" role="img" aria-label="Starry night sky over Earth with a bright sunrise on the horizon">
  <div class="hero-text">
    <h1 class="hero-title">BRINDLE</h1>
    <p class="hero-sub">Lorem Ipsum is simply dummy</p>
    <a class="btn btn-crimson" href="#">Contact us now</a>
  </div>
</section>

<section class="services">
  <div class="service">
    <svg class="service-icon" viewBox="0 0 94 94"><path d="M12 60A38 38 0 0 1 60 12" fill="none" stroke="var(--yellow)" stroke-width="4"/><rect x="40" y="30" width="14" height="10" fill="var(--yellow)"/><rect x="26" y="56" width="12" height="10" fill="var(--yellow)"/><rect x="56" y="56" width="12" height="10" fill="var(--yellow)"/><path d="M47 40v8M32 56v-8h30v8" fill="none" stroke="var(--yellow)" stroke-width="3"/></svg>
    <div><h3>Planning &amp;<br>Buying</h3><p>Lorem Ipsum is simply dummy of the printing and type.</p></div>
  </div>
  <div class="service">
    <svg class="service-icon" viewBox="0 0 94 94"><path d="M12 60A38 38 0 0 1 60 12" fill="none" stroke="var(--blue)" stroke-width="4"/><rect x="26" y="44" width="30" height="22" fill="none" stroke="var(--blue)" stroke-width="3"/><path d="M31 62v-6M38 62v-10M45 62v-8M52 62v-12" stroke="var(--blue)" stroke-width="3"/><path d="M28 40l10-8 8 5 14-11" fill="none" stroke="var(--blue)" stroke-width="3"/></svg>
    <div><h3>Data &amp;<br>Insights</h3><p>Lorem Ipsum is simply dummy of the printing and type.</p></div>
  </div>
  <div class="service">
    <svg class="service-icon" viewBox="0 0 94 94"><path d="M12 60A38 38 0 0 1 60 12" fill="none" stroke="var(--grey-ring)" stroke-width="4"/><rect x="24" y="38" width="42" height="28" rx="3" fill="none" stroke="#444" stroke-width="3"/><circle cx="40" cy="52" r="7" fill="none" stroke="#444" stroke-width="3"/><path d="M54 46h8M54 52h8M54 58h8" stroke="#444" stroke-width="2"/></svg>
    <div><h3>Media &amp;<br>Strategy</h3><p>Lorem Ipsum is simply dummy of the printing and type.</p></div>
  </div>
  <div class="service">
    <svg class="service-icon" viewBox="0 0 94 94"><path d="M12 60A38 38 0 0 1 60 12" fill="none" stroke="var(--crimson)" stroke-width="4"/><path d="M28 66v-10M35 66v-16M42 66v-12" stroke="#444" stroke-width="4"/><circle cx="54" cy="52" r="8" fill="none" stroke="#444" stroke-width="3"/><path d="M60 58l8 8" stroke="#444" stroke-width="3"/><path d="M26 44l10-10 6 5 10-9" fill="none" stroke="var(--crimson)" stroke-width="3"/></svg>
    <div><h3>Seo</h3><p>Lorem Ipsum is simply dummy of the printing and type.</p></div>
  </div>
</section>

<section class="welcome">
  <h2 class="section-title">WELCOME TO <span>BRINDLE</span></h2>
  <p>We make your brand famous. To do this we optimise your website or any digital assets you have, so they can be found online, whether that is through search engines or social media. Then we make sure your paid media is as efficient as possible. Your customer lives in the real world as well as online, so we have no restrictions. We work with our clients across organic search, paid search, display and social media as well as television...</p>
  <a class="btn btn-crimson" href="#">Read more <svg width="14" height="12" viewBox="0 0 14 12"><path d="M1 1l5 5-5 5M7 1l5 5-5 5" fill="none" stroke="#fff" stroke-width="2"/></svg></a>
  <div class="welcome-mark">Brindle</div>
</section>

<section class="work">
  <h2 class="section-title">OUR WORK</h2>
  <p class="lead">Lorem Ipsum is simply dummy text of the printing and typesetting industry. Lorem Ipsum has been.</p>
  <div class="work-grid">
    <article class="work-card">
      <div class="work-photo" role="img" aria-label="Fashion shoot of two women in bold coats against a red and white backdrop" style="background:linear-gradient(90deg,#3a2a24,#c8c2bc 45%,#b8212a 75%,#e6e6e6)"></div>
      <h3>Lorem Ipsum is simply</h3>
      <p>Lorem Ipsum is simply dummy text<br>of the printing and typesetting industry.<br>Lorem Ipsum has... &nbsp;READ MORE »</p>
    </article>
    <article class="work-card">
      <div class="work-photo" role="img" aria-label="Red hot air balloons floating in a golden yellow sky" style="background:linear-gradient(160deg,#ffd21a,#f5a400 60%,#e07b00)"></div>
      <h3>Lorem Ipsum is simply</h3>
      <p>Lorem Ipsum is simply dummy text<br>of the printing and typesetting industry.<br>Lorem Ipsum has... &nbsp;READ MORE »</p>
    </article>
    <article class="work-card">
      <div class="work-photo" role="img" aria-label="Athlete crouching in a dim tunnel" style="background:linear-gradient(90deg,#9a9a9a,#4a4e50 50%,#1c1e20)"></div>
      <h3>Lorem Ipsum is simply</h3>
      <p>Lorem Ipsum is simply dummy text<br>of the printing and typesetting industry.<br>Lorem Ipsum has... &nbsp;READ MORE »</p>
    </article>
  </div>
</section>

<section class="clients" aria-label="Clients and memberships">
  <span class="client" style="color:#c2185b"><i style="background:#c2185b"></i>Hollings Marlowe</span>
  <span class="client" style="color:#2e7d32"><i style="background:#2e7d32"></i>Cobble Loans</span>
  <span class="badge badge-navy"></span>
  <span class="badge badge-black"></span>
  <span class="client"><i></i>The Gripwell Academy</span>
  <span class="client" style="color:#6d2f8e"><i style="background:#6d2f8e"></i>Lunglight UK</span>
</section>

<section class="who">
  <h2 class="section-title">WHO WE ARE</h2>
  <p class="lead">Are their decisions based on what is best for your brand or are there other incentives involved?</p>
  <div class="video" role="img" aria-label="Embedded video: Brindle Media — Who We Are, with a city tower sketch and intro text"><span class="video-play"></span></div>
  <div class="who-copy">
    <div class="who-badges"><span class="badge badge-navy"></span><span class="badge badge-black"></span></div>
    <p>We are Brindle Media</p>
    <p>We believe...</p>
    <p>There are too many large agency networks. Consolidation is everywhere, giving clients less choice and choking media creativity for the benefit of perceived economies of scale.</p>
    <a class="btn btn-white" href="#">Read more <svg width="14" height="12" viewBox="0 0 14 12"><path d="M1 1l5 5-5 5M7 1l5 5-5 5" fill="none" stroke="#9b1536" stroke-width="2"/></svg></a>
  </div>
</section>

<section class="blog">
  <h2 class="section-title">BLOG</h2>
  <div class="blog-grid">
    <article class="post">
      <div class="post-photo" role="img" aria-label="Street scene with a person walking past a red storefront" style="background:linear-gradient(180deg,#c2452d,#e8d9c8 70%,#bfb7ad)"></div>
      <h3>Lorem Ipsum is simply dummy text of the printing.</h3>
      <time>▦ October 27, 2016</time>
      <p>Lorem Ipsum is simply dummy text of the printing and typesetting industry.</p>
    </article>
    <article class="post">
      <div class="post-photo" role="img" aria-label="Team meeting around a bright office table" style="background:linear-gradient(180deg,#e9ecef,#b9c3cc 60%,#8d99a5)"></div>
      <h3>Lorem Ipsum is simply dummy text of the printing.</h3>
      <time>▦ October 27, 2016</time>
      <p>Lorem Ipsum is simply dummy text of the printing and typesetting industry.</p>
    </article>
    <article class="post">
      <div class="post-photo" role="img" aria-label="Wall of glowing digital screens" style="background:linear-gradient(160deg,#0c3a4f,#1f8fb0 50%,#0a1a25)"></div>
      <h3>Lorem Ipsum is simply dummy text of the printing.</h3>
      <time>▦ October 27, 2016</time>
      <p>Lorem Ipsum is simply dummy text of the printing and typesetting industry.</p>
    </article>
    <article class="post">
      <div class="post-photo" role="img" aria-label="Two colleagues reviewing work at a desk" style="background:linear-gradient(180deg,#f3f4f6,#c9ced6 60%,#3c4350)"></div>
      <h3>Lorem Ipsum is simply dummy text of the printing.</h3>
      <time>▦ October 27, 2016</time>
      <p>Lorem Ipsum is simply dummy text of the printing and typesetting industry.</p>
    </article>
  </div>
</section>

<footer class="footer">
  <div class="footer-nav">
    <nav class="footer-links"><a href="#">Home</a><a href="#">About</a><a href="#">Our Work</a><a href="#">Who We Are</a><a href="#">Client Login</a><a href="#">Contact</a></nav>
    <div class="footer-social" aria-label="Social links"><span></span><span></span><span></span><span></span></div>
  </div>
  <h4>Contact Us</h4>
  <div class="contact-row">
    <div class="contact-item"><span class="contact-icon red"><svg width="16" height="20" viewBox="0 0 16 20"><path d="M8 0a7 7 0 0 0-7 7c0 5 7 13 7 13s7-8 7-13a7 7 0 0 0-7-7z" fill="#fff"/><circle cx="8" cy="7" r="2.6" fill="#9b1536"/></svg></span>14 Calder Row<br>London, W1X 9QZ</div>
    <div class="contact-item"><span class="contact-icon"><svg width="14" height="20" viewBox="0 0 14 20"><rect x="1" y="1" width="12" height="18" rx="2" fill="none" stroke="#000" stroke-width="2"/><circle cx="7" cy="15.5" r="1.2"/></svg></span>+44 207 555 0143</div>
    <div class="contact-item"><span class="contact-icon"><svg width="20" height="18" viewBox="0 0 20 18"><rect x="1" y="6" width="18" height="11" rx="2" fill="none" stroke="#000" stroke-width="2"/><rect x="5" y="1" width="10" height="6" fill="none" stroke="#000" stroke-width="2"/><path d="M5 11h10M5 14h6" stroke="#000" stroke-width="1.6"/></svg></span>2345678 - 90</div>
    <div class="contact-item"><span class="contact-icon"><svg width="20" height="14" viewBox="0 0 20 14"><rect x="1" y="1" width="18" height="12" fill="none" stroke="#000" stroke-width="2"/><path d="M1 1l9 7 9-7" fill="none" stroke="#000" stroke-width="2"/></svg></span>contact@brindle-media.example</div>
  </div>
</footer>
<div class="copyright">©&nbsp;<b>Brindle - 2016.</b>&nbsp; All Rights Reserved.</div>

</body>
</html>
```